Business Card design for construction company

I would like a business card design for a construction company - Harlow Constructions. I have attached the ai logo file for use. I would like the card to be very smart and clean and incorporate only white and the two colours in the logo. I would like the card to have two sides. One side can just have the logo, the other with the relevant information.

Target Market(s)

Building and Construction Clients

Industry/Entity Type

Business

Contact Information for Business Card

Name: Tom Pardoe
Company: Harlow Constructions Pty Limited
Address: 14 Mallee Crescent Carrow Vale 2093
Phone: 0427 531 068
Email: tomp@harlowbuild-example.com.au

Font styles to use
Serif
Sans Serif

Requirements
Must have
• Details noted above
• Logo as provided
• Colours as in logo
• Square edges
• A font that compliments the logo
Should not have
• Any colour other than white and those in logo
• Rounded edges

```html
<!DOCTYPE html>
<html lang="en">
<head>
<meta charset="utf-8">
<title>Harlow Constructions – Business Card</title>
<link rel="stylesheet" href="https://fonts.googleapis.com/css2?family=Arimo:wght@400&display=swap">
<style>
  :root {
    --stage: #4a4a4c;
    --card: #f4f4f2;
    --ink: #4a4a4a;
    --accent: #2aa3dc;
  }
  * { margin: 0; padding: 0; box-sizing: border-box; }
  html, body {
    width: 1200px;
    height: 1200px;
    overflow: hidden;
    background: var(--stage);
    font-family: "Arimo", Arial, sans-serif;
  }
  .stage {
    width: 1200px;
    height: 1200px;
    display: flex;
    flex-direction: column;
    align-items: center;
    justify-content: center;
    gap: 60px;
  }
  .card {
    width: 760px;
    height: 465px;
    background: var(--card);
    position: relative;
  }
  /* Front side */
  .card--front {
    display: flex;
    align-items: center;
    justify-content: center;
  }
  .brand-name {
    font-size: 34px;
    letter-spacing: 6px;
    text-transform: uppercase;
    color: var(--ink);
    font-weight: 400;
  }
  /* Back side */
  .card--back {
    display: flex;
    align-items: center;
    padding-left: 70px;
  }
  .identity {
    text-align: right;
    padding-right: 20px;
  }
  .person-name {
    font-size: 40px;
    color: var(--ink);
    line-height: 1.1;
  }
  .company-name {
    font-size: 15px;
    color: var(--accent);
    margin-top: 6px;
  }
  .divider {
    width: 4px;
    height: 112px;
    background: var(--accent);
  }
  .contact-list {
    list-style: none;
    padding-left: 22px;
  }
  .contact-item {
    display: flex;
    align-items: center;
    gap: 12px;
    font-size: 16px;
    color: var(--ink);
    line-height: 1;
    margin: 9px 0;
  }
  .contact-icon {
    width: 16px;
    height: 16px;
    flex: none;
  }
</style>
</head>
<body>
<main class="stage">
  <section class="card card--front" aria-label="Business card front">
    <p class="brand-name">Harlow Constructions</p>
  </section>

  <section class="card card--back" aria-label="Business card back">
    <div class="identity">
      <h1 class="person-name">Tom Pardoe</h1>
      <p class="company-name">Harlow Constructions Pty Limited</p>
    </div>
    <div class="divider"></div>
    <ul class="contact-list">
      <li class="contact-item">
        <svg class="contact-icon" viewBox="0 0 16 16" aria-hidden="true">
          <path d="M8 1a5 5 0 0 0-5 5c0 3.6 5 9 5 9s5-5.4 5-9a5 5 0 0 0-5-5z" fill="#2aa3dc"/>
          <circle cx="8" cy="6" r="1.8" fill="#f4f4f2"/>
        </svg>
        <span>14 Mallee Crescent Carrow Vale 2093</span>
      </li>
      <li class="contact-item">
        <svg class="contact-icon" viewBox="0 0 16 16" aria-hidden="true">
          <circle cx="8" cy="8" r="8" fill="#2aa3dc"/>
          <path d="M5.2 4.2l1.4 1.8-.8 1c.6 1.2 1.4 2 2.6 2.6l1-.8 1.8 1.4-.9 1.4c-2.9-.4-5.2-2.7-5.6-5.6z" fill="#f4f4f2"/>
        </svg>
        <span>0427 531 068</span>
      </li>
      <li class="contact-item">
        <svg class="contact-icon" viewBox="0 0 16 16" aria-hidden="true">
          <circle cx="8" cy="8" r="8" fill="#2aa3dc"/>
          <rect x="4" y="5.3" width="8" height="5.4" fill="#f4f4f2"/>
          <path d="M4 5.3l4 3 4-3" fill="none" stroke="#2aa3dc" stroke-width="0.9"/>
        </svg>
        <span>tomp@harlowbuild-example.com.au</span>
      </li>
    </ul>
  </section>
</main>
</body>
</html>
```